Corvalith business website

I am wanting a website for my media agency Corvalith.

It needs to be be an attractive, unique and professional looking website. The website is a destination for people to be able to understand the service that Corvalith offers.

Please read uploaded website copy to gain an understanding of the business.

Target Market(s)

small business owners, business decision makers, marketing managers,

Industry/Entity Type

Business

Requirements
Must have
• Good branding.

```html
<!DOCTYPE html>
<html lang="en">
<head>
<meta charset="utf-8">
<title>Corvalith — Media Strategy, Planning and Buying</title>
<link href="https://fonts.googleapis.com/css2?family=Questrial&family=Ubuntu:wght@400;500&display=swap" rel="stylesheet">
<style>
:root{
  --violet:#5a48e6;
  --sky:#00a9ea;
  --teal:#7ecbc4;
  --teal-dark:#3ea99e;
  --green:#a5d49b;
  --green-dark:#5fae57;
  --orange:#ff6e2b;
  --orange-dark:#e8491a;
  --sand:#f5f4f1;
  --ink:#1b1e2b;
  --ink-deep:#0b0d14;
  --grey-text:#8f9095;
  --body-text:#5d5e63;
  --rss:#f9a51a;
  --bird:#1da1e0;
  --book:#1a4fa0;
  --white:#fff;
}
*{margin:0;padding:0;box-sizing:border-box}
html,body{width:826px;height:1200px;overflow:hidden;background:var(--white)}
body{position:relative;font-family:"Questrial",sans-serif;color:var(--body-text)}
.abs{position:absolute}

.brand{left:83px;top:8px;display:flex;align-items:center;gap:7px}
.brand-square{width:14px;height:14px;background:var(--violet)}
.brand-name{font-size:17px;color:var(--violet)}
.nav{left:293px;top:16px;width:533px;height:32px;background:var(--violet);
  clip-path:polygon(12px 0,100% 0,100% 100%,12px 100%,0 50%);
  display:flex;align-items:center;padding-left:48px;gap:36px}
.nav a{color:var(--white);text-decoration:none;font-size:11.5px;letter-spacing:.2px}

.hero{left:0;top:64px;width:826px;height:294px}
.hero-photo{left:90px;top:143px;width:262px;height:211px;border-radius:120px 120px 0 0;
  background:linear-gradient(180deg,#7a5a48 0%,#c49a80 45%,#8fa3c4 100%)}
.hero-icons{left:232px;top:96px}
.hero-title{left:310px;top:198px;color:var(--white);font-size:19px;line-height:22px;text-transform:uppercase}
.hero-title b{font-weight:400;font-family:"Ubuntu",sans-serif;font-weight:500}
.hero-copy{left:486px;top:199px;width:262px;color:var(--white);font-size:11px;line-height:14px}

.service{width:142px;text-align:center}
.service-tile{width:142px;height:125px;display:flex;align-items:center;justify-content:center;border-bottom:4px solid}
.service-title{font-size:9.8px;line-height:14px;text-transform:uppercase;margin:20px 0 10px}
.service-text{font-size:8.6px;line-height:13px;color:var(--body-text)}
.bracket{width:142px;height:8px}

.why-band{left:0;top:766px;width:826px;height:290px;background:var(--sand)}
.section-title{font-family:"Ubuntu",sans-serif;font-size:16.5px;color:#55565c;text-transform:uppercase}
.lead{font-size:9.4px;line-height:15.6px;color:var(--orange)}
.muted{font-size:9.4px;line-height:15.6px;color:var(--grey-text)}
.partner{background:#cfcfd2;border-radius:4px}

.newsletter-title{left:93px;top:1062px;font-family:"Ubuntu",sans-serif;font-size:15.5px;color:var(--white);text-transform:uppercase}
.newsletter-text{left:93px;top:1090px;font-size:8.7px;color:#c7c8cf}
.email{left:93px;top:1121px;width:349px;height:48px;background:var(--ink-deep);display:flex;align-items:center;justify-content:space-between;padding:0 22px 0 25px;color:var(--white);font-size:12.5px}
.social{top:1066px;width:39px;height:36px;border-bottom:3px solid rgba(0,0,0,.25)}
</style>
</head>
<body>

<header>
  <div class="abs brand"><span class="brand-square"></span><span class="brand-name">Corvalith</span></div>
  <nav class="abs nav"><a href="#">ABOUT</a><a href="#">WHAT WE DO</a><a href="#">PEOPLE</a><a href="#">IDEAS</a><a href="#">CONTACT US</a></nav>
</header>

<section>
  <svg class="abs hero" width="826" height="294" viewBox="0 0 826 294" aria-hidden="true">
    <path d="M0 0H826V259Q413 330 0 259Z" fill="var(--sky)"/>
  </svg>
  <div class="abs hero-photo" role="img" aria-label="Photo of a thoughtful woman looking up at ideas"></div>
  <svg class="abs hero-icons" width="460" height="70" viewBox="0 0 460 70" fill="none" stroke="#fff" stroke-width="2.4" aria-hidden="true">
    <circle cx="30" cy="36" r="10" fill="#fff" stroke="none"/><rect x="23" y="46" width="9" height="6" fill="#fff" stroke="none" transform="rotate(30 27 49)"/>
    <rect x="70" y="8" width="22" height="28" rx="2" transform="rotate(-12 81 22)"/>
    <rect x="128" y="8" width="38" height="22" rx="2" transform="rotate(12 147 19)"/><circle cx="147" cy="19" r="6"/>
    <path d="M210 30q0-10 14-10t14 10-14 10q-4 0-6-1l-6 4 1-6q-3-3-3-7z" fill="#fff" stroke="none"/>
    <path d="M288 28v12l-8 14h20l-8-14V28" />
    <circle cx="354" cy="28" r="8"/><circle cx="354" cy="28" r="13" stroke-dasharray="4 4" stroke-width="4"/><circle cx="376" cy="36" r="5"/>
    <path d="M422 8v30h36M428 36V22M435 36V14M442 36V24M449 36V28"/>
  </svg>
  <h1 class="abs hero-title">Corvalith is a<br><b>media strategy,</b><br>planning and<br><b>buying agency</b></h1>
  <p class="abs hero-copy">We work with both small and big businesses. Corvalith works across all offline platforms (radio, press, outdoor &amp; TV), search engine marketing, online display, email, social &amp; mobile. We attain a high level of value for our clients with a focus on integration.</p>
</section>

<section>
  <article class="abs service" style="left:123px;top:421px">
    <div class="service-tile" style="background:var(--teal);border-color:var(--teal-dark)">
      <svg width="44" height="54" viewBox="0 0 44 54" fill="none" stroke="#fff" stroke-width="3" aria-hidden="true"><path d="M14 8H4v42h30V28M30 8h4v8"/><rect x="13" y="4" width="14" height="8" rx="2"/><path d="M16 36l8 8 18-24"/></svg>
    </div>
    <h2 class="service-title" style="color:var(--teal-dark)">Media strategy and<br>planning</h2>
    <p class="service-text">Using accurate analysis we provide relevant research about the consumer or business target &amp; trends in the market place.<br>A tailored strategy is devised that comprises of the right media channels that fit with the target &amp; business network.</p>
  </article>
  <svg class="abs bracket" style="left:123px;top:719px" viewBox="0 0 142 8" aria-hidden="true"><path d="M1 0v3h67l3 4 3-4h67V0" fill="none" stroke="var(--teal-dark)" stroke-width="3"/></svg>

  <article class="abs service" style="left:343px;top:395px">
    <div class="service-tile" style="background:var(--green);border-color:var(--green-dark)">
      <svg width="54" height="40" viewBox="0 0 54 40" fill="#fff" aria-hidden="true"><rect x="0" y="14" width="6" height="12"/><path d="M8 14l34-12v36L8 26z"/><rect x="46" y="2" width="5" height="36"/><rect x="14" y="26" width="10" height="8"/></svg>
    </div>
    <h2 class="service-title" style="color:var(--green-dark)">Media trading &amp; campaign<br>monitoring</h2>
    <p class="service-text">Using our media partner relationships, trade negotiation techniques &amp; experience we achieve a high level of value for all media buys that leads to significant cost savings for clients. All media activity is monitored &amp; optimized to ensure performance.</p>
  </article>
  <svg class="abs bracket" style="left:343px;top:693px" viewBox="0 0 142 8" aria-hidden="true"><path d="M1 0v3h67l3 4 3-4h67V0" fill="none" stroke="var(--green-dark)" stroke-width="3"/></svg>

  <article class="abs service" style="left:563px;top:421px">
    <div class="service-tile" style="background:var(--orange);border-color:var(--orange-dark)">
      <svg width="32" height="54" viewBox="0 0 32 54" fill="#fff" aria-hidden="true"><path d="M16 0a16 16 0 0 1 9 29v9H7v-9A16 16 0 0 1 16 0z"/><rect x="7" y="41" width="18" height="3"/><rect x="7" y="46" width="18" height="3"/><rect x="11" y="51" width="10" height="3"/></svg>
    </div>
    <h2 class="service-title" style="color:var(--orange)">Content &amp; creative</h2>
    <p class="service-text">Creating imaginative &amp; interesting content for a brand can be a great way of achieving a high level of engagement to a target audience. Content can be published and broadcast on a variety of different media platforms. We also happily create awesome ads across all formats.</p>
  </article>
  <svg class="abs bracket" style="left:563px;top:719px" viewBox="0 0 142 8" aria-hidden="true"><path d="M1 0v3h67l3 4 3-4h67V0" fill="none" stroke="var(--orange-dark)" stroke-width="3"/></svg>
</section>

<section>
  <div class="abs why-band"></div>
  <h2 class="abs section-title" style="left:83px;top:797px">Why use Corvalith?</h2>
  <p class="abs lead" style="left:83px;top:824px;width:300px">Lorem ipsum dolor sit amet, consectetur adipiscing elit. Nullam lacus felis, sagittis id hendrerit nec, facilisis non ligula. Nullam eget imperdiet augue. Suspendisse lacus nulla, tempor eget porta a, accumsan at erat. Etiam quis sem orci.</p>
  <p class="abs muted" style="left:83px;top:900px;width:300px">Lorem ipsum dolor sit amet, consectetur adipiscing elit. Nullam lacus felis, sagittis id hendrerit nec, facilisis non ligula. Nullam eget imperdiet augue. Suspendisse lacus nulla, tempor eget porta a, accumsan at erat. Etiam quis sem orci. Praesent elit sem, volutpat id malesuada a, ornare non turpis. Aliquam felis ante, condimentum eu tempor eu, dapibus ut lacus.</p>

  <h2 class="abs section-title" style="left:445px;top:797px">Our partners</h2>
  <p class="abs lead" style="left:445px;top:824px;width:300px">Lorem ipsum dolor sit amet, consectetur adipiscing elit. Nullam lacus felis, sagittis id hendrerit nec, facilisis non ligula. Nullam eget imperdiet augue.</p>
  <div class="abs partner" style="left:447px;top:878px;width:113px;height:30px"></div>
  <div class="abs partner" style="left:580px;top:876px;width:62px;height:34px"></div>
  <div class="abs partner" style="left:666px;top:873px;width:50px;height:40px"></div>
  <div class="abs partner" style="left:448px;top:932px;width:82px;height:42px"></div>
  <div class="abs partner" style="left:556px;top:933px;width:46px;height:42px"></div>
</section>

<footer>
  <svg class="abs" style="left:0;top:1011px" width="826" height="189" viewBox="0 0 826 189" aria-hidden="true">
    <path d="M0 33Q413 -30 826 33V189H0Z" fill="var(--ink)"/>
  </svg>
  <h2 class="abs newsletter-title">Subscribe our newsletter</h2>
  <p class="abs newsletter-text">Lorem ipsum dolor sit amet, consectetur adipiscing elit. Nullam lacus felis sagittis id</p>
  <div class="abs email"><span>Leave your email</span>
    <svg width="20" height="14" viewBox="0 0 20 14" fill="none" stroke="#fff" stroke-width="1.4" aria-hidden="true"><rect x="1" y="1" width="18" height="12"/><path d="M1 1l9 7 9-7"/></svg>
  </div>
  <a class="abs social" href="#" aria-label="Feed" style="left:602px;background:var(--rss)"></a>
  <a class="abs social" href="#" aria-label="Microblog" style="left:653px;background:var(--bird)"></a>
  <a class="abs social" href="#" aria-label="Social network" style="left:704px;background:var(--book)"></a>
</footer>

</body>
</html>
```